Brazilian wine business need a label for a sparkling wine

We are importing a new italian sparkling wine, but we need to build our own brand. Our main focus is to sell sparkling wine for events, specially for weddings. So, specially for this audience, presentation is key.
We like to see wine in a "uncomplicated" way.
It is a mid price product.
The foil capsule color must be black, white or silver, due to production restrictions. We cannot have any graphic interference in this part, also.

We need to develop a label for it. The name will be "Lumera Brut" (means "hug" in italian).

Our main public is people around the early 30s, so it should look modern and clean.
It is good, but not mandatory, to have a few information at the front label:
- Alcohol % (12%)
- Origin (Italy)

We need to avoid a few colours, for different reasons:
- Don´t use yellow/orange: too linked to Maison Dravelle;
- Don´t use red or pink: people think it is a rosé, but it is a white.
Our idea is to work with white and blue or turquoise, maybe a green, something like that. Can have a touch of gold, also. (more references in the color tab below)
- The bottle is black.

Industry/Entity Type

Business

Font styles to use
Other font styles liked:
• Berlin Sans FB Regular or something less "round" but similar to Cooper Black Regular

Colors
00a990
33b8a4

Requirements
Must have
• As the name means "hug", we want to have a graphic symbol that represents connections, alliances, symbiosis or infinite. I attached a few symbols that could be explore, but of course you can bring differente suggestions.
• We need a clean design, nothing with too many information.

```html
<!DOCTYPE html>
<html lang="en">
<head>
<meta charset="utf-8">
<title>Lumera Brut – Sparkling Wine Label</title>
<link href="https://fonts.googleapis.com/css2?family=Libre+Baskerville:wght@400&display=swap" rel="stylesheet">
<style>
  :root {
    --canvas: #ffffff;
    --bottle: #1c1418;
    --bottle-edge: #2b2126;
    --foil: #0f0d0e;
    --label: #ffffff;
    --turquoise: #33b8a4;
    --teal: #00a990;
    --band: #3fb3c4;
    --gold: #c9a24a;
    --ink: #1f1f1f;
  }
  html, body {
    margin: 0;
    padding: 0;
    width: 1200px;
    height: 3781px;
    overflow: hidden;
    background: var(--canvas);
  }
  .bottle-art { display: block; width: 1200px; height: 3781px; }
  .bottle-glass { fill: var(--bottle); stroke: var(--bottle-edge); stroke-width: 6; }
  .foil-capsule { fill: var(--foil); }
  .label-paper { fill: var(--label); }
  .shoulder-band { fill: none; stroke: var(--band); stroke-width: 36; }
  .shoulder-name {
    font-family: "Libre Baskerville", serif;
    font-size: 46px;
    fill: var(--gold);
    letter-spacing: 3px;
  }
  .body-mark { fill: none; stroke: var(--teal); stroke-width: 6; }
  .body-brand {
    font-family: "Libre Baskerville", serif;
    font-size: 40px;
    fill: var(--teal);
    letter-spacing: 3px;
  }
  .rule { stroke: var(--band); stroke-width: 14; }
  .product-name {
    font-family: "Libre Baskerville", serif;
    font-size: 104px;
    fill: var(--band);
    letter-spacing: 4px;
  }
  .fine-print {
    font-family: "Libre Baskerville", serif;
    font-size: 26px;
    fill: var(--ink);
  }
</style>
</head>
<body>
<svg class="bottle-art" viewBox="0 0 1200 3781" xmlns="http://www.w3.org/2000/svg">
  <defs>
    <path id="bottle-outline" d="M430,40 Q430,0 470,0 L730,0 Q770,0 770,40 L780,1050 C790,1350 1080,1700 1085,2350 L1085,3690 Q1085,3740 1035,3740 L165,3740 Q115,3740 115,3690 L115,2350 C120,1700 410,1350 420,1050 Z"/>
    <clipPath id="bottle-clip">
      <use href="#bottle-outline"/>
    </clipPath>
    <linearGradient id="damask-fill" x1="0" y1="0" x2="0" y2="1">
      <stop offset="0" stop-color="#f4f5f6"/>
      <stop offset="1" stop-color="#e9ecee"/>
    </linearGradient>
    <linearGradient id="lace-fill" x1="0" y1="0" x2="0" y2="1">
      <stop offset="0" stop-color="#ffffff"/>
      <stop offset="1" stop-color="#cfe9f0"/>
    </linearGradient>
  </defs>

  <!-- Bottle -->
  <use class="bottle-glass" href="#bottle-outline"/>

  <g clip-path="url(#bottle-clip)">
    <!-- Plain foil capsule -->
    <path class="foil-capsule" d="M400,0 L800,0 L800,1000 L400,1000 Z"/>

    <!-- Shoulder label -->
    <g class="shoulder-label">
      <path class="label-paper" d="M0,1690 Q600,1620 1200,1690 L1200,1960 Q850,1940 600,2050 Q350,1940 0,1960 Z"/>
      <rect role="img" aria-label="Faint damask ornament pattern on shoulder label" x="0" y="1660" width="1200" height="210" fill="url(#damask-fill)" opacity="0.7"/>
      <text class="shoulder-name" x="600" y="1810" text-anchor="middle">LUMERA BRUT</text>
      <path class="shoulder-band" d="M0,1880 Q330,1850 600,1995 Q870,1850 1200,1880"/>
    </g>

    <!-- Body label -->
    <g class="body-label">
      <path class="label-paper" d="M100,2660 Q360,2620 600,2670 Q840,2620 1100,2660 L1100,3590 L100,3590 Z"/>
      <rect role="img" aria-label="Faint damask ornament pattern behind the brand" x="100" y="2690" width="1000" height="270" fill="url(#damask-fill)" opacity="0.8"/>
      <circle class="body-mark" cx="390" cy="2826" r="22"/>
      <text class="body-brand" x="430" y="2840">LUMERA BRUT</text>

      <line class="rule" x1="100" y1="2990" x2="1100" y2="2990"/>
      <text class="product-name" x="600" y="3100" text-anchor="middle" textLength="880" lengthAdjust="spacingAndGlyphs">LUMERA BRUT</text>
      <line class="rule" x1="100" y1="3130" x2="1100" y2="3130"/>

      <text class="fine-print" x="140" y="3180">Alc. 12% by vol.</text>
      <text class="fine-print" x="1060" y="3180" text-anchor="end">0.75l</text>

      <rect role="img" aria-label="Light blue lace ornament border" x="100" y="3210" width="1000" height="380" fill="url(#lace-fill)"/>
    </g>
  </g>
</svg>
</body>
</html>
```